Infographic Table of AI Pricing Options for LinkedIn post

Turn this table (in the powerpoint slide attached) into an attractively formatted infographic table for Solqarin (www.solqarin.com).
This will be an infographic displayed on a linkedin post from a consultant from Solqarin.
Try to keep it on brand with Solqarin look and feel.

Target Market(s)

Tech and SaaS CEOs and Founders; Private Equity and Venture Capital employees

Industry/Entity Type

Management Consulting

Colors
0054AA
0677BA
7BADD7
CADEEF
E8F1F8

```html
<!DOCTYPE html>
<html lang="en">
<head>
<meta charset="utf-8">
<title>Challenges of GenAI Monetization — Solqarin</title>
<link rel="stylesheet" href="https://fonts.googleapis.com/css2?family=Lexend:wght@400;500;600;700&family=Inter:wght@400;500;600&display=swap">
<style>
:root{
  --bg-top:#14232e;
  --bg-bottom:#05080b;
  --glow:#1f7a73;
  --panel:#101c25;
  --panel-edge:#1a2a35;
  --bar:#1f3240;
  --white:#ffffff;
  --muted:#c9d6df;
  --accent-blue:#4aa8dc;
  --accent-teal:#2fb5a6;
  --head-1:#4aa9db;
  --head-2:#2886be;
  --head-3:#2ba89c;
  --head-4:#2d6c8e;
  --col-1:#1d3a50;
  --col-2:#17415c;
  --col-3:#1c4a56;
  --col-4:#27394a;
  --divider:rgba(255,255,255,.14);
  --tick:#59c46c;
  --cross:#4aa8dc;
}
*{margin:0;padding:0;box-sizing:border-box}
html,body{width:1200px;height:927px;overflow:hidden}
body{
  font-family:"Inter",sans-serif;color:var(--white);
  background:
    radial-gradient(520px 300px at 1080px 940px, rgba(47,181,166,.45), transparent 70%),
    radial-gradient(600px 400px at 200px 120px, rgba(40,80,100,.35), transparent 70%),
    linear-gradient(180deg,var(--bg-top),var(--bg-bottom));
  position:relative;
}
.title{position:absolute;left:70px;top:46px;font-family:"Lexend",sans-serif;font-weight:600;font-size:58px;line-height:70px;letter-spacing:-.5px}
.title .hl{color:var(--accent-blue)}
.brand{position:absolute;left:884px;top:58px;display:flex;align-items:center;gap:12px;font-family:"Lexend",sans-serif;font-size:36px;font-weight:400}
.brand-mark{width:46px;height:46px;background:var(--accent-blue);border-radius:6px}
.panel{position:absolute;left:68px;top:225px;width:1065px;height:640px;background:var(--panel);border-radius:22px;border:1px solid var(--panel-edge)}
.top-strip{position:absolute;left:128px;top:222px;width:488px;height:52px;background:#0c161e;border-radius:0 0 14px 14px}
.top-strip span{position:absolute;left:10px;width:466px;height:8px;background:var(--bar);border-radius:4px}
.intro{position:absolute;left:638px;top:240px;font-size:14px;line-height:18px;color:var(--muted);width:420px}
.intro b{color:var(--white);font-weight:600}
.intro-dot{position:absolute;left:1085px;top:246px;width:22px;height:20px;background:var(--accent-teal);border-radius:4px;outline:7px solid #0c161e}
.corner-tile{position:absolute;left:67px;top:820px;width:54px;height:45px;border-radius:9px;background:linear-gradient(135deg,var(--accent-blue),var(--accent-teal))}
.group-label{position:absolute;top:306px;font-size:15px;font-weight:500}
.group-label.now{left:266px;color:var(--accent-blue)}
.group-label.future{right:90px;color:var(--accent-teal)}
.row-label{position:absolute;left:70px;font-family:"Lexend",sans-serif;font-size:20px;font-weight:500}
.row-band{position:absolute;left:68px;width:196px;background:#142431;border-radius:2px}
.column{position:absolute;top:331px;width:206px;height:518px;border-radius:14px;overflow:hidden}
.column header{height:64px;display:flex;align-items:center;justify-content:center;text-align:center;font-family:"Lexend",sans-serif;font-size:19px;font-weight:500;line-height:22px;text-transform:uppercase}
.cell{position:absolute;left:0;width:100%;border-top:1px solid var(--divider);font-size:11.5px;line-height:16px}
.desc{top:64px;height:85px;padding:16px 18px 0 20px}
.examples{top:149px;height:90px;display:flex;flex-direction:column;align-items:center;justify-content:center;gap:14px}
.pros{top:239px;height:120px;padding:12px 14px 0 20px}
.cons{top:359px;height:159px;padding:12px 14px 0 20px}
.name{display:flex;align-items:center;gap:7px;font-family:"Lexend",sans-serif;font-weight:600;font-size:14px}
.name i{width:20px;height:20px;background:rgba(255,255,255,.22);border-radius:4px;display:block}
ul{list-style:none}
li{display:flex;gap:8px;margin-bottom:10px}
li svg{flex:none;margin-top:2px}
.c1{left:264px;background:var(--col-1)} .c1 header{background:var(--head-1)}
.c2{left:479px;background:var(--col-2)} .c2 header{background:var(--head-2)}
.c3{left:694px;background:var(--col-3)} .c3 header{background:var(--head-3)}
.c4{left:909px;background:var(--col-4)} .c4 header{background:var(--head-4)}
</style>
</head>
<body>
<svg width="0" height="0" style="position:absolute">
  <symbol id="tick" viewBox="0 0 14 14"><circle cx="7" cy="7" r="6" fill="none" stroke="#59c46c" stroke-width="1.3"/><path d="M4 7.2l2 2 4-4.2" fill="none" stroke="#59c46c" stroke-width="1.4" stroke-linecap="round" stroke-linejoin="round"/></symbol>
  <symbol id="cross" viewBox="0 0 14 14"><circle cx="7" cy="7" r="6" fill="none" stroke="#4aa8dc" stroke-width="1.3"/><path d="M4.8 4.8l4.4 4.4M9.2 4.8l-4.4 4.4" stroke="#4aa8dc" stroke-width="1.4" stroke-linecap="round"/></symbol>
</svg>

<h1 class="title">Challenges of<br><span class="hl">GenAI</span> Monetization</h1>
<div class="brand"><span class="brand-mark"></span>Solqarin</div>

<div class="panel"></div>
<div class="top-strip"><span style="top:4px"></span><span style="top:20px"></span><span style="top:36px"></span></div>
<p class="intro">There are <b>3 major monetization models</b> that have begun to gain traction with AI, and one we expect to see more of</p>
<div class="intro-dot"></div>
<div class="corner-tile"></div>

<div class="group-label now">Frequently seen today</div>
<div class="group-label future">Future option?</div>

<div class="row-band" style="top:434px;height:44px"></div>
<div class="row-band" style="top:517px;height:50px"></div>
<div class="row-band" style="top:606px;height:82px"></div>
<div class="row-band" style="top:727px;height:80px"></div>
<div class="row-label" style="top:402px">Description</div>
<div class="row-label" style="top:486px">Examples</div>
<div class="row-label" style="top:574px">Pros</div>
<div class="row-label" style="top:695px">Cons</div>

<section class="column c1">
  <header>User<br>Licenses</header>
  <div class="cell desc">Charge a flat price for a user to have access to the functionality</div>
  <div class="cell examples"><span class="name"><i></i>ChatNova</span><span class="name"><i></i>CoGuide</span></div>
  <div class="cell pros"><ul><li><svg width="14" height="14"><use href="#tick"/></svg>Simple and easily understood</li></ul></div>
  <div class="cell cons"><ul>
    <li><svg width="14" height="14"><use href="#cross"/></svg>High price limits adoption</li>
    <li><svg width="14" height="14"><use href="#cross"/></svg>Not tightly value aligned</li>
    <li><svg width="14" height="14"><use href="#cross"/></svg>Risky if fair usage restriction is not placed on</li>
    <li><svg width="14" height="14"><use href="#cross"/></svg>Upsell dependent on wider adoption</li>
  </ul></div>
</section>

<section class="column c2">
  <header>Usage-Based<br>Tokens</header>
  <div class="cell desc">Purchase blocks of tokens that can be spend on usage/work of the AI functionality</div>
  <div class="cell examples"><span class="name"><i></i>Veridex</span><span class="name"><i></i>Optiscan Vision API</span></div>
  <div class="cell pros"><ul>
    <li><svg width="14" height="14"><use href="#tick"/></svg>Covers costs at all scales of usage</li>
    <li><svg width="14" height="14"><use href="#tick"/></svg>Tokens help with predictability issues</li>
  </ul></div>
  <div class="cell cons"><ul>
    <li><svg width="14" height="14"><use href="#cross"/></svg>Not tightly value aligned (value may not increase linearly with usage)</li>
    <li><svg width="14" height="14"><use href="#cross"/></svg>Not ARR</li>
  </ul></div>
</section>

<section class="column c3">
  <header>Outcome<br>Based</header>
  <div class="cell desc">Pay for the outcomes of the GenAI functionality</div>
  <div class="cell examples"><span class="name"><i></i>disputely</span><span class="name"><i></i>helpnest</span></div>
  <div class="cell pros"><ul><li><svg width="14" height="14"><use href="#tick"/></svg>Potentially highly value-aligned</li></ul></div>
  <div class="cell cons"><ul>
    <li><svg width="14" height="14"><use href="#cross"/></svg>Delayed revenue realization</li>
    <li><svg width="14" height="14"><use href="#cross"/></svg>Tough to find the right metric</li>
    <li><svg width="14" height="14"><use href="#cross"/></svg>Not ARR</li>
  </ul></div>
</section>

<section class="column c4">
  <header>Usage-Tiered<br>Licenses</header>
  <div class="cell desc">Offer different user licenses with different usage capacities</div>
  <div class="cell examples"><span class="name"><i></i>ChatNova</span></div>
  <div class="cell pros"><ul>
    <li><svg width="14" height="14"><use href="#tick"/></svg>Value aligned</li>
    <li><svg width="14" height="14"><use href="#tick"/></svg>Simple &amp; predictable</li>
    <li><svg width="14" height="14"><use href="#tick"/></svg>Natural upsell path</li>
    <li><svg width="14" height="14"><use href="#tick"/></svg>Low barrier to adoption</li>
  </ul></div>
  <div class="cell cons"><ul><li><svg width="14" height="14"><use href="#cross"/></svg>Limit on the number of tiers</li></ul></div>
</section>
</body>
</html>
```